SMP by Dana Holloway - Scalp Micropigmentation

I need a wordpress site designed for me, can be based off a theme, I already have a logo and the press site ready to be created, I can provide a login for you. I will be able to update it myself with content I just need the layout done as Im having trouble with it. I want to be able to add pages as needed and have a gallery for my work.

Target Market(s)

customers

Coding

Coded - Design and coding required

Number of Pages Required

5+ page

Font styles to use
Sans Serif

Colors

Designer to choose colors to be used in the design.

Requirements
Must have
• my logo, wordpress, gallery
Should not have
• shopping cart

```html
<!DOCTYPE html>
<html lang="en">
<head>
<meta charset="utf-8">
<title>SMP by Dana Holloway – Scalp Micropigmentation</title>
<link rel="stylesheet" href="https://fonts.googleapis.com/css2?family=Montserrat:wght@300;400;500;600&family=Open+Sans:wght@400;600;700&display=swap">
<style>
:root{
  --ink:#1d1d1d;
  --text:#555;
  --muted:#777;
  --accent:#4fa3db;
  --pale:#eef3f7;
  --line:#d7d7d7;
  --footer:#1f1c1c;
  --star:#f4d03f;
}
*{box-sizing:border-box;margin:0;padding:0}
html,body{width:1200px;height:4215px;overflow:hidden;background:#fff}
body{position:relative;font-family:"Open Sans",Arial,sans-serif;color:var(--text)}
.abs{position:absolute}
h1,h2,h3,h4{font-family:"Montserrat",Arial,sans-serif;font-weight:400;color:var(--ink)}

/* header */
.site-header{left:0;top:0;width:1200px;height:112px;background:#fff}
.brand{left:112px;top:42px;font-family:"Montserrat",sans-serif;font-size:20px;font-weight:500;color:var(--ink);letter-spacing:1px;white-space:nowrap}
.nav{right:112px;top:46px;display:flex;gap:26px;font-size:15px;color:#333;align-items:center}
.nav .active{color:var(--accent)}

/* hero */
.hero{left:0;top:112px;width:1200px;height:591px;background:linear-gradient(90deg,#e8e8e8 0%,#e2e2e2 50%,#d9d6d3 100%)}
.hero-photo{left:560px;top:112px;width:640px;height:591px;background:radial-gradient(ellipse at 55% 45%,#c9b3a4 0%,#b49a89 35%,#d8d3cf 75%,#e0dfde 100%)}
.hero-title{left:112px;top:282px;font-size:52px;line-height:70px;font-weight:500;letter-spacing:3px;color:var(--ink)}
.btn-solid{left:112px;top:523px;width:253px;height:56px;background:var(--accent);color:#fff;font-size:15px;font-weight:600;display:flex;align-items:center;justify-content:center;letter-spacing:.5px}
.slide-arrow{width:36px;height:44px;background:rgba(150,150,150,.75);display:flex;align-items:center;justify-content:center}

/* welcome */
.welcome-title{left:112px;top:808px;font-size:36px;line-height:48px}
.body-copy{font-size:14px;line-height:26px;color:var(--text)}
.btn-outline{border:2px solid var(--accent);color:var(--accent);font-size:13px;font-weight:600;display:flex;align-items:center;justify-content:center;letter-spacing:.5px}
.divider-v{left:651px;top:871px;width:1px;height:170px;background:var(--line)}
.feature-icon{width:84px;height:84px;border-radius:50%;border:2px solid #ddd;display:flex;align-items:center;justify-content:center;background:#fff}
.feature-title{font-family:"Montserrat",sans-serif;font-size:21px;color:var(--ink);letter-spacing:1px}
.feature-text{font-size:13px;color:var(--muted);margin-top:6px}

/* services */
.services{left:0;top:1203px;width:1200px;height:730px;background:var(--pale)}
.section-title{width:1200px;left:0;text-align:center;font-size:39px;letter-spacing:1px}
.card{width:309px;height:430px;background:#fff;border:1px solid #dcdcdc;box-shadow:0 1px 4px rgba(0,0,0,.08)}
.card-photo{width:100%;height:210px}
.card h3{text-align:center;font-size:24px;margin-top:36px;letter-spacing:1px}
.card p{text-align:center;font-size:13px;line-height:24px;color:var(--muted);padding:0 26px;margin-top:14px}
.card .more{text-align:center;font-size:13px;font-weight:600;color:var(--accent);margin-top:14px}

/* transformations */
.transform-frame{left:500px;top:2043px;width:588px;height:444px;border:2px solid #cfcfcf}
.transform-photo{left:112px;top:2091px;width:450px;height:345px;background:linear-gradient(90deg,#d2cdc9,#bcb0a6 50%,#c8bdb3)}
.transform-title{left:612px;top:2108px;font-size:39px;letter-spacing:1px}

/* testimonials */
.testimonials{left:0;top:2599px;width:1200px;height:540px;background:linear-gradient(135deg,#5fa9d8,#4f9dd2 50%,#62acd9)}
.quote-card{width:306px;height:245px;border:2px solid rgba(255,255,255,.85);text-align:center;color:#fff}
.quote-card p{font-size:13px;line-height:23px;font-style:italic;padding:62px 28px 0}
.quote-card h4{color:#fff;font-family:"Open Sans",sans-serif;font-weight:600;font-size:17px;margin-top:12px}
.stars{margin-top:14px;display:flex;justify-content:center}
.avatar{width:86px;height:86px;border-radius:50%;border:4px solid #fff;background:linear-gradient(#d9c2ad,#a98e7b)}
.round-arrow{width:48px;height:48px;border-radius:50%;display:flex;align-items:center;justify-content:center}

/* gallery */
.gallery-photo{top:3344px;height:205px}

/* footer */
.site-footer{left:0;top:3675px;width:1200px;height:540px;background:var(--footer)}
.footer-title{font-family:"Montserrat",sans-serif;font-size:21px;color:#fff;letter-spacing:1px}
.field{background:#fff;border:1px solid #ccc;font-size:11px;color:#777;padding:8px 10px}
.btn-submit{left:643px;top:4032px;width:99px;height:43px;background:var(--accent);color:#fff;font-size:13px;font-weight:700;display:flex;align-items:center;justify-content:center}
.info-row{left:804px;display:flex;align-items:center;gap:22px;color:#fff;font-size:13px;line-height:22px}
.info-icon{width:34px;height:34px;border-radius:50%;border:1px solid #888;display:flex;align-items:center;justify-content:center;flex:none}
.social{width:34px;height:34px;border-radius:50%}
.footer-rule{left:100px;top:4120px;width:1000px;height:1px;background:#3d3939}
.copyright{left:0;top:4150px;width:1200px;text-align:center;color:#ddd;font-size:13px}
</style>
</head>
<body>

<header class="site-header abs">
  <div class="brand abs">SMP by Dana Holloway</div>
  <nav class="nav abs">
    <span class="active">Home</span><span>About</span><span>Treatments</span><span>Gallery</span><span>Training</span><span>Transformations</span><span>Blog</span><span>Contact</span>
    <svg width="16" height="16" viewBox="0 0 16 16"><circle cx="6.5" cy="6.5" r="4.5" fill="none" stroke="#222" stroke-width="2"/><line x1="10" y1="10" x2="14" y2="14" stroke="#222" stroke-width="2"/></svg>
  </nav>
</header>

<section class="hero abs"></section>
<div class="hero-photo abs" role="img" aria-label="Photo of a man with a shaved head and a drawn hairline showing a micropigmentation treatment"></div>
<h1 class="hero-title abs">SCALP<br>MICRO<br>PIGMENTATION</h1>
<div class="btn-solid abs">GET FREE CONSULTATION</div>
<div class="slide-arrow abs" style="left:0;top:386px"><svg width="12" height="18"><polyline points="9,2 3,9 9,16" fill="none" stroke="#fff" stroke-width="2"/></svg></div>
<div class="slide-arrow abs" style="right:0;top:386px"><svg width="12" height="18"><polyline points="3,2 9,9 3,16" fill="none" stroke="#fff" stroke-width="2"/></svg></div>

<section class="welcome">
  <h2 class="welcome-title abs">WELCOME TO SCALP<br>MICRO PIGMENTATION</h2>
  <p class="body-copy abs" style="left:112px;top:926px;width:470px">Nemo enim ipsam voluptatem quia voluptas sit aspernatur aut odit aut fugit, sed quia consequuntur magni dolores eos qui ratione voluptatem sequi nesciu iquam est, qui dolorem ipsum.</p>
  <div class="btn-outline abs" style="left:112px;top:1043px;width:124px;height:42px">READ MORE</div>
  <div class="divider-v abs"></div>

  <div class="feature-icon abs" style="left:734px;top:807px"><svg width="40" height="26"><rect x="1" y="1" width="38" height="24" rx="2" fill="#e7a23a"/><circle cx="20" cy="13" r="7" fill="#fff"/><rect x="5" y="5" width="30" height="16" fill="none" stroke="#fff" stroke-width="1.5"/></svg></div>
  <div class="abs" style="left:843px;top:822px"><div class="feature-title">AFFORDABLE</div><div class="feature-text">At vero eos et accusamus et iusto odio</div></div>

  <div class="feature-icon abs" style="left:734px;top:911px"><svg width="36" height="34" viewBox="0 0 36 34"><rect x="2" y="14" width="8" height="18" fill="#6ab04c"/><path d="M12 14 L20 2 Q24 2 23 8 L22 12 H32 Q35 13 34 17 L31 30 Q30 32 27 32 H12 Z" fill="#6ab04c"/></svg></div>
  <div class="abs" style="left:843px;top:924px"><div class="feature-title">PERMANENT</div><div class="feature-text">At vero eos et accusamus et iusto odio</div></div>

  <div class="feature-icon abs" style="left:734px;top:1012px"><svg width="40" height="40" viewBox="0 0 40 40"><polygon points="20,2 24,8 31,6 31,13 38,16 34,21 38,27 31,29 30,36 23,34 20,39 16,34 9,36 9,29 2,27 6,21 2,16 9,13 9,6 16,8" fill="#3d8fd1"/><circle cx="20" cy="20" r="8" fill="#5aa8e0"/></svg></div>
  <div class="abs" style="left:843px;top:1024px"><div class="feature-title">GUARANTEED</div><div class="feature-text">At vero eos et accusamus et iusto odio</div></div>
</section>

<section class="services abs"></section>
<h2 class="section-title abs" style="top:1296px">WHAT WE DO</h2>
<article class="card abs" style="left:112px;top:1391px">
  <div class="card-photo" role="img" aria-label="Artist tattooing a hairline on a client's scalp" style="background:linear-gradient(135deg,#b59783,#8c8f9a)"></div>
  <h3>HAIRLINE</h3>
  <p>Nam libero tempore, cum soluta nob est eligendi optio cumque nihil impedit quo minus id quod maxime placea</p>
  <div class="more">READ MORE</div>
</article>
<article class="card abs" style="left:446px;top:1391px">
  <div class="card-photo" role="img" aria-label="Close-up of a pigmentation needle over a scar on the scalp" style="background:linear-gradient(135deg,#d1c3b6,#a9a3a0)"></div>
  <h3>SCAR CAMOUFLAGE</h3>
  <p>Nam libero tempore, cum soluta nob est eligendi optio cumque nihil impedit quo minus id quod maxime placea</p>
  <div class="more">READ MORE</div>
</article>
<article class="card abs" style="left:780px;top:1391px">
  <div class="card-photo" role="img" aria-label="Gloved hands treating pattern baldness on a scalp" style="background:linear-gradient(135deg,#4a4a4c,#2a2a2c 60%,#6d6361)"></div>
  <h3>PATTERN BALDNESS</h3>
  <p>Nam libero tempore, cum soluta nob est eligendi optio cumque nihil impedit quo minus id quod maxime placea</p>
  <div class="more">READ MORE</div>
</article>

<section class="transformations">
  <div class="transform-frame abs"></div>
  <div class="transform-photo abs" role="img" aria-label="Before and after comparison of a scalp treatment, viewed from behind"></div>
  <h2 class="transform-title abs">TRANSFORMATIONS</h2>
  <p class="body-copy abs" style="left:614px;top:2177px;width:440px">Nemo enim ipsam voluptatem quia voluptas sit aspernatur aut odit aut fugit, sed quia consequuntur magni dolores eos qui ratione volu ptatem sequi nesciu iquam est, qui dolorem ipsum loptas assunda eomnis dolor repellendus. Temporibus autem quibusdam et aut cis debitis aut rerum necessitatibus saepe.</p>
  <div class="btn-outline abs" style="left:614px;top:2349px;width:126px;height:44px">READ MORE</div>
</section>

<section class="testimonials abs"></section>
<h2 class="section-title abs" style="top:2680px;color:#fff">TESTIMONIALS</h2>
<div class="quote-card abs" style="left:112px;top:2804px"><p>Nam libero tempore, cum soluta nobis est eligendi optio cumque nihil impedit quo minus id quod maxime placea</p><h4>Nora Whitfield</h4><div class="stars"><svg width="90" height="16"><g fill="var(--star)"><polygon points="8,0 10,6 16,6 11,10 13,16 8,12 3,16 5,10 0,6 6,6"/><polygon transform="translate(18 0)" points="8,0 10,6 16,6 11,10 13,16 8,12 3,16 5,10 0,6 6,6"/><polygon transform="translate(36 0)" points="8,0 10,6 16,6 11,10 13,16 8,12 3,16 5,10 0,6 6,6"/><polygon transform="translate(54 0)" points="8,0 10,6 16,6 11,10 13,16 8,12 3,16 5,10 0,6 6,6"/><polygon transform="translate(72 0)" points="8,0 10,6 16,6 11,10 13,16 8,12 3,16 5,10 0,6 6,6"/></g></svg></div></div>
<div class="quote-card abs" style="left:447px;top:2804px"><p>Nam libero tempore, cum soluta nobis est eligendi optio cumque nihil impedit quo minus id quod maxime placea</p><h4>Tessa Brandt</h4><div class="stars"><svg width="90" height="16"><g fill="var(--star)"><polygon points="8,0 10,6 16,6 11,10 13,16 8,12 3,16 5,10 0,6 6,6"/><polygon transform="translate(18 0)" points="8,0 10,6 16,6 11,10 13,16 8,12 3,16 5,10 0,6 6,6"/><polygon transform="translate(36 0)" points="8,0 10,6 16,6 11,10 13,16 8,12 3,16 5,10 0,6 6,6"/><polygon transform="translate(54 0)" points="8,0 10,6 16,6 11,10 13,16 8,12 3,16 5,10 0,6 6,6"/><polygon transform="translate(72 0)" points="8,0 10,6 16,6 11,10 13,16 8,12 3,16 5,10 0,6 6,6"/></g></svg></div></div>
<div class="quote-card abs" style="left:782px;top:2804px"><p>Nam libero tempore, cum soluta nobis est eligendi optio cumque nihil impedit quo minus id quod maxime placea</p><h4>Owen Marsh</h4><div class="stars"><svg width="90" height="16"><g fill="var(--star)"><polygon points="8,0 10,6 16,6 11,10 13,16 8,12 3,16 5,10 0,6 6,6"/><polygon transform="translate(18 0)" points="8,0 10,6 16,6 11,10 13,16 8,12 3,16 5,10 0,6 6,6"/><polygon transform="translate(36 0)" points="8,0 10,6 16,6 11,10 13,16 8,12 3,16 5,10 0,6 6,6"/><polygon transform="translate(54 0)" points="8,0 10,6 16,6 11,10 13,16 8,12 3,16 5,10 0,6 6,6"/><polygon transform="translate(72 0)" points="8,0 10,6 16,6 11,10 13,16 8,12 3,16 5,10 0,6 6,6"/></g></svg></div></div>
<div class="avatar abs" role="img" aria-label="Portrait of client Nora Whitfield" style="left:222px;top:2759px"></div>
<div class="avatar abs" role="img" aria-label="Portrait of client Tessa Brandt" style="left:557px;top:2759px"></div>
<div class="avatar abs" role="img" aria-label="Portrait of client Owen Marsh" style="left:892px;top:2759px"></div>
<div class="round-arrow abs" style="left:27px;top:2901px;border:2px solid #fff"><svg width="12" height="16"><polyline points="9,2 3,8 9,14" fill="none" stroke="#fff" stroke-width="2"/></svg></div>
<div class="round-arrow abs" style="left:1125px;top:2901px;border:2px solid #fff"><svg width="12" height="16"><polyline points="3,2 9,8 3,14" fill="none" stroke="#fff" stroke-width="2"/></svg></div>

<section class="gallery">
  <h2 class="section-title abs" style="top:3243px">GALLERY</h2>
  <div class="gallery-photo abs" role="img" aria-label="Top of a treated scalp" style="left:112px;width:240px;background:linear-gradient(135deg,#e6e3e1,#b69d8c)"></div>
  <div class="gallery-photo abs" role="img" aria-label="Smiling client after treatment by the sea" style="left:360px;width:235px;background:linear-gradient(180deg,#9cc4de,#c8a890)"></div>
  <div class="gallery-photo abs" role="img" aria-label="Artist working on a client in the studio" style="left:604px;width:237px;background:linear-gradient(135deg,#8ea3b4,#b08e7a)"></div>
  <div class="gallery-photo abs" role="img" aria-label="Close-up of a pigmented scalp" style="left:851px;width:237px;background:linear-gradient(135deg,#3a2f2a,#8a6e5c 60%,#5b4a40)"></div>
  <div class="round-arrow abs" style="left:33px;top:3423px;border:2px solid #999"><svg width="12" height="16"><polyline points="9,2 3,8 9,14" fill="none" stroke="#666" stroke-width="2"/></svg></div>
  <div class="round-arrow abs" style="left:1121px;top:3423px;border:2px solid #999"><svg width="12" height="16"><polyline points="3,2 9,8 3,14" fill="none" stroke="#666" stroke-width="2"/></svg></div>
</section>

<footer class="site-footer abs"></footer>
<h3 class="footer-title abs" style="left:112px;top:3766px">CONTACT FORM</h3>
<div class="field abs" style="left:112px;top:3838px;width:310px;height:34px">First Name</div>
<div class="field abs" style="left:432px;top:3838px;width:310px;height:34px">Last Name</div>
<div class="field abs" style="left:112px;top:3883px;width:310px;height:34px">Email</div>
<div class="field abs" style="left:432px;top:3883px;width:310px;height:34px">Phone Number</div>
<div class="field abs" style="left:112px;top:3931px;width:630px;height:82px">Comments</div>
<div class="btn-submit abs">SUBMIT</div>

<h3 class="footer-title abs" style="left:804px;top:3766px">CONTACT INFORMATION</h3>
<div class="info-row abs" style="top:3833px"><span class="info-icon"><svg width="12" height="16" viewBox="0 0 12 16"><path d="M6 0C2.7 0 0 2.6 0 5.8 0 10 6 16 6 16s6-6 6-10.2C12 2.6 9.3 0 6 0z" fill="#fff"/><circle cx="6" cy="6" r="2.2" fill="#1f1c1c"/></svg></span><span>2210 Cedar Grove Lane<br>Fairview, Oregon 97024</span></div>
<div class="info-row abs" style="top:3897px"><span class="info-icon"><svg width="16" height="16" viewBox="0 0 16 16"><path d="M3 1l3 3-2 2c1 2 3 4 5 5l2-2 3 3-2 3C7 15 1 9 1 3z" fill="#fff"/></svg></span><span>1 555 010 2040</span></div>
<div class="info-row abs" style="top:3957px"><span class="info-icon"><svg width="16" height="12" viewBox="0 0 16 12"><rect width="16" height="12" rx="1" fill="#fff"/><polyline points="1,1 8,7 15,1" fill="none" stroke="#1f1c1c" stroke-width="1.5"/></svg></span><span>hello@smpstudio.example</span></div>
<div class="abs" style="left:804px;top:4021px;display:flex;gap:10px">
  <span class="social" style="background:#3b5998"></span>
  <span class="social" style="background:#c9803f"></span>
  <span class="social" style="background:#dd4b39"></span>
  <span class="social" style="background:#cb2027"></span>
</div>
<div class="footer-rule abs"></div>
<p class="copyright abs">Copyright © 2018, Scalp Micro Pigmentation. All rights reserved.</p>

</body>
</html>
```